New Digital Marketing Company Needs Web Design

Introduction

Brightcrest gives advice to small businesses about their websites and digital marketing strategies and builds working relationships with clients to understand their business and maximise its online presence.

Brightcrest offers services to support its clients needs such as: website auditing & search engine optimisation (SEO), Quorvo Promoline, Chatterlane advertising, newsletter development & management, online performance reporting, email setup & management, website hosting, maintenance & backup, web development, web updates & web design.

Design Specification

The site should have a clean & professional look and use the colour scheme from the logo (attached below).

The design should consist of 2 templates; The homepage & content page.

Homepage Design

The homepage should have a header with logo, contact number and email and menu. Followed underneath by a slider and then individual blocks for key services. Under the key services should be a testimonial block with 3 testimonials. Finally the footer with company details, menu links and location map.

Header Info:

Contact number: 01632 960481
Email: info@brightcrest-demo.co.uk

Menu: Home Services About Contact

Slider Design:

The slider should be full page and show an image with text.

Key Services:

The key services should have a relevant icon and brief description.

The key services are:

Digital Marketing

Website Hosting & Management

Website Health Check (SEO)

Website Updating & Development

Newsletter Management

Email Management

Note: Lorem Ipsum can be used for brief description...

Testimonials:

There should be 3 testimonials side by side and they should include a headshot image of the person giving the testimonial.

Note: Lorem Ipsum and sample images can be used for testimonials...

Footer:

The footer should have 3 sections:

Menu links:

Digital Marketing About
Quorvo Promoline Contact
Chatterlane Advertising Privacy Policy
Search Engine Optimisation (SEO) Terms & Conditions
Website Hosting FAQ
Newsletter Management

Company Information:

BrightCrest
14 Marlow Close
Bracknell
Berskhire
ZZ9 4QT
Tel: 01632 960481

Chatterlane icon - Pipwave icon - Careernest icon

Location

Quorvo map

Footer Bottom:

Copyright message.

Content Design

The content design should have the common header and footer.

Each content page should have a banner for image with text description (page title).

The content page should have area for text description and area for a video display if available.

There should be a right column (possibly) for modules (latest blog, latest Chatterlane feeds, testimonial)

Project Deadline Extended
Reason: I have had to extend the deadline as could not review while on vacation and need to feedback to some designers for content page design. Many thanks for your understanding.

Target Market(s)

Industry/Entity Type

Digital

Number of Pages Required

2 page

Requirements
Must have
• The site should have a clean & professional look and use the colour scheme from the logo (attached below).
• The design should consist of 2 templates; The homepage & content page.

```html
<!DOCTYPE html>
<html lang="en">
<head>
<meta charset="utf-8">
<title>BrightCrest – Home</title>
<link href="https://fonts.googleapis.com/css2?family=Open+Sans:wght@400;600;700;800&family=Roboto:wght@400;500&family=Oswald:wght@400&display=swap" rel="stylesheet">
<style>
:root{
  --indigo:#473d6a;
  --plum:#6b1850;
  --plum-band:#6a1a4e;
  --ink:#333;
  --light:#efefef;
  --footer:#1e1e1e;
  --footer-text:#9a9a9a;
  --white:#fff;
}
*{box-sizing:border-box;margin:0;padding:0}
html,body{width:1200px;height:2500px;overflow:hidden}
body{font-family:'Roboto',Arial,sans-serif;color:var(--ink);background:var(--white);position:relative}
.abs{position:absolute}
h1,h2,h3,h4{font-family:'Open Sans',Arial,sans-serif}

/* header */
.site-header{position:absolute;left:0;top:0;width:1200px;height:100px;background:var(--white)}
.brand{left:130px;top:16px;display:flex;align-items:center;gap:10px}
.brand-dot{width:40px;height:40px;border-radius:50%;background:var(--indigo)}
.brand-name{font-family:'Open Sans',sans-serif;font-weight:700;font-size:38px;color:var(--indigo);letter-spacing:-0.5px}
.contact-item{top:14px;display:flex;align-items:center;gap:10px;font-family:'Oswald',sans-serif;font-size:17px;color:var(--indigo)}
.contact-icon{width:24px;height:24px;border-radius:50%;background:var(--indigo);display:flex;align-items:center;justify-content:center}
.main-nav{left:728px;top:58px;display:flex;height:40px}
.main-nav a{font-family:'Open Sans',sans-serif;font-weight:600;font-size:13px;color:#222;text-decoration:none;display:flex;align-items:center;padding:0 24px}
.main-nav a.active{background:var(--plum);color:var(--white);padding:0 17px;margin-right:10px}

/* slider */
.hero{position:absolute;left:0;top:100px;width:1200px;height:490px;overflow:hidden}
.hero-photo{left:0;top:0;width:1200px;height:490px;
  background:
    radial-gradient(ellipse 260px 300px at 430px 230px,#fbfbfb 0%,rgba(251,251,251,0) 100%),
    linear-gradient(90deg,#4a4a52 0%,#8d8f96 9%,#d2d2d4 18%,#ececec 34%,#f1f1f1 55%,#ebebeb 75%,#e2e2e2 100%)}
.hero-title{left:756px;top:122px;font-family:'Open Sans',sans-serif;font-size:52px;line-height:52px;text-transform:uppercase}
.hero-title .lead{color:var(--indigo);font-weight:400;display:block}
.hero-title .strong{color:var(--plum);font-weight:800;display:block;letter-spacing:-1px}
.btn{display:inline-flex;align-items:center;gap:8px;background:var(--indigo);color:var(--white);font-family:'Open Sans',sans-serif;font-weight:700;font-size:14px;text-transform:uppercase}
.hero .btn{position:absolute;left:763px;top:313px;height:49px;padding:0 20px;font-size:16px}
.slide-arrow{top:228px;width:38px;height:45px;background:#5a5178;display:flex;align-items:center;justify-content:center}
.dots{left:546px;top:441px;display:flex;gap:13px}
.dots span{width:9px;height:9px;border-radius:50%;background:#555}
.dots span.on{background:transparent;border:1.5px solid #555;width:11px;height:11px;margin-top:-1px}

/* services */
.services{position:absolute;left:0;top:590px;width:1200px;height:613px;background:var(--indigo);overflow:hidden}
.section-title{font-weight:700;font-size:26px;color:var(--white);text-align:center;width:1200px;top:33px}
.title-rule{left:563px;top:80px;width:74px;height:3px;background:var(--white)}
.service-card{width:294px;height:217px;border:1.5px solid rgba(255,255,255,0.3);text-align:center;color:var(--white);padding-top:22px}
.service-card svg{display:block;margin:0 auto 14px}
.service-card h3{font-size:16px;font-weight:600;line-height:20px;margin-bottom:14px}
.service-card p{font-size:12.5px;line-height:18px;color:rgba(255,255,255,0.85);padding:0 38px}

/* welcome */
.welcome{position:absolute;left:0;top:1203px;width:1200px;height:414px;background:var(--light)}
.welcome h2{left:132px;top:53px;font-size:21px;font-weight:700;color:var(--indigo);text-transform:uppercase}
.welcome .h-rule{left:132px;top:87px;width:240px;height:3px;background:var(--indigo)}
.welcome-text{left:132px;top:117px;width:390px;font-size:12.5px;line-height:20px;color:#444;text-align:justify}
.welcome-text p+p{margin-top:20px}
.welcome .btn{position:absolute;left:132px;top:298px;height:40px;padding:0 15px;font-size:12px}
.video{left:572px;top:42px;width:496px;height:330px;background:#222}
.video-frame{width:496px;height:297px;background:linear-gradient(135deg,#b9c3cc 0%,#7b8896 40%,#3b4656 75%,#222a36 100%)}
.play{left:208px;top:108px;width:76px;height:76px;border-radius:50%;background:rgba(255,255,255,0.9);display:flex;align-items:center;justify-content:center}
.progress{left:0;top:297px;width:496px;height:4px;background:#555}
.progress span{display:block;width:6px;height:4px;background:var(--plum)}
.controls{left:0;top:301px;width:496px;height:29px;display:flex;align-items:center;gap:14px;padding:0 12px;font-size:10px;color:#ddd}

/* modules */
.modules{position:absolute;left:0;top:1617px;width:1200px;height:496px;background:var(--plum-band)}
.module{top:40px;width:305px;height:416px;background:var(--white);padding:16px 16px}
.module h2{font-size:21px;font-weight:700;color:var(--indigo);text-transform:uppercase;line-height:26px}
.blog-item,.quote-item{position:absolute;left:16px;width:273px;height:90px;border:1px solid #ccc;display:flex}
.thumb{width:106px;height:88px;flex:none}
.blog-body{padding:12px 10px 0 12px;font-size:10.5px}
.blog-body .date{color:#555;font-size:10px}
.blog-body h4{font-family:'Roboto',sans-serif;font-size:12px;font-weight:500;color:#111;margin:3px 0 4px}
.blog-body p{color:#666;line-height:14px;font-size:10px}
.module .btn{position:absolute;right:16px;top:367px;height:32px;padding:0 13px;font-size:11.5px}
.headshot{width:76px;height:88px;flex:none}
.quote-body{padding:8px 10px 0 12px;position:relative;flex:1}
.quote-mark{position:absolute;left:5px;top:0;font-family:Georgia,serif;font-size:26px;color:#bbb}
.quote-body p{font-size:11px;line-height:15px;color:#333;padding-left:12px;padding-top:6px}
.quote-body .who{position:absolute;right:8px;bottom:5px;font-size:9px;font-weight:500;color:var(--indigo);text-transform:uppercase}
.feed-tag{right:16px;top:20px;width:58px;height:16px;background:#44579a}
.feed-item{position:absolute;left:16px;width:273px;height:78px;border-bottom:1px solid #ddd;display:flex;gap:12px;padding-top:2px}
.feed-thumb{width:28px;height:28px;flex:none;margin-top:6px}
.feed-item h4{font-family:'Roboto',sans-serif;font-weight:400;font-size:11px;line-height:15px;color:#3b5998}
.feed-item p{font-size:9.5px;color:#888;margin-top:6px}
.plugin-bar{left:0;bottom:0;width:305px;height:40px;border-top:2px solid #ccc;padding:12px 18px;font-size:8.5px;color:#888;display:flex;gap:6px;align-items:center}
.plugin-bar span{width:10px;height:10px;background:#44579a;display:inline-block}

/* footer */
.site-footer{position:absolute;left:0;top:2113px;width:1200px;height:387px;background:var(--footer);color:var(--footer-text);font-size:11px}
.site-footer h4{font-size:11.5px;font-weight:700;color:var(--white);text-transform:uppercase}
.footer-menu{left:132px;top:55px}
.footer-menu ul{list-style:none;margin-top:14px;line-height:21px}
.company{left:480px;top:55px}
.company address{font-style:normal;margin-top:14px;line-height:21px}
.social{left:480px;top:224px;display:flex;gap:11px}
.social span{width:32px;height:32px;border-radius:50%;display:block}
.map{left:718px;top:54px;width:350px;height:200px;background:linear-gradient(160deg,#cfe3b8 0%,#e9ecd8 45%,#bfdca4 100%)}
.footer-rule{left:132px;top:309px;width:936px;height:1px;background:#3a3a3a}
.copyright{left:0;top:338px;width:1200px;text-align:center;font-size:10.5px}
</style>
</head>
<body>

<header class="site-header">
  <div class="abs brand"><span class="brand-dot"></span><span class="brand-name">BrightCrest</span></div>
  <div class="abs contact-item" style="left:728px">
    <span class="contact-icon"><svg width="12" height="12" viewBox="0 0 24 24"><path fill="#fff" d="M6.6 10.8a15 15 0 0 0 6.6 6.6l2.2-2.2c.3-.3.7-.4 1-.2 1.1.4 2.3.6 3.6.6.6 0 1 .4 1 1V20c0 .6-.4 1-1 1A17 17 0 0 1 3 4c0-.6.4-1 1-1h3.5c.6 0 1 .4 1 1 0 1.3.2 2.5.6 3.6.1.3 0 .7-.2 1z"/></svg></span>01632 960481</div>
  <div class="abs contact-item" style="left:885px">
    <span class="contact-icon"><svg width="12" height="10" viewBox="0 0 24 18"><path fill="#fff" d="M0 0h24v2L12 10 0 2zM0 5l12 8 12-8v13H0z"/></svg></span>info@brightcrest-demo.co.uk</div>
  <nav class="abs main-nav">
    <a class="active">HOME</a><a>SERVICES</a><a>ABOUT</a><a>CONTACT</a>
  </nav>
</header>

<section class="hero">
  <div class="abs hero-photo" role="img" aria-label="Slider photo: a hand in a dark suit sleeve sketching a light bulb full of business doodles on a pale grey wall"></div>
  <h1 class="abs hero-title"><span class="lead">Advice to</span><span class="strong">Small</span><span class="strong">Businesses</span></h1>
  <a class="btn">Read more <svg width="12" height="12" viewBox="0 0 12 12"><path d="M1 1l5 5-5 5M6 1l5 5-5 5" stroke="#fff" stroke-width="1.6" fill="none"/></svg></a>
  <div class="abs slide-arrow" style="left:0"><svg width="10" height="16" viewBox="0 0 10 16"><path d="M8 1L2 8l6 7" stroke="#fff" stroke-width="2" fill="none"/></svg></div>
  <div class="abs slide-arrow" style="left:1162px"><svg width="10" height="16" viewBox="0 0 10 16"><path d="M2 1l6 7-6 7" stroke="#fff" stroke-width="2" fill="none"/></svg></div>
  <div class="abs dots"><span></span><span class="on"></span><span></span><span></span><span></span></div>
</section>

<section class="services">
  <h2 class="abs section-title">OUR SERVICES</h2>
  <div class="abs title-rule"></div>

  <article class="abs service-card" style="left:132px;top:118px">
    <svg width="54" height="46" viewBox="0 0 54 46" fill="none" stroke="#fff" stroke-width="2.4"><path d="M6 16h10l22-12v34L16 26H6z"/><path d="M12 26l4 14h6l-3-14"/><path d="M44 15c3 3 3 9 0 12M48 10c6 6 6 16 0 22"/></svg>
    <h3>Digital Marketing</h3>
    <p>At vero eos et accusamus et iusto odio dignissimos ducimus qui blanditiis praesentium voluptatum.</p>
  </article>
  <article class="abs service-card" style="left:453px;top:118px">
    <svg width="54" height="46" viewBox="0 0 54 46" fill="none" stroke="#fff" stroke-width="2.4"><rect x="6" y="2" width="42" height="12" rx="2"/><rect x="6" y="17" width="42" height="12" rx="2"/><rect x="6" y="32" width="42" height="12" rx="2"/><path d="M12 8h14M12 23h14M12 38h14"/><circle cx="40" cy="8" r="1.5" fill="#fff"/><circle cx="40" cy="23" r="1.5" fill="#fff"/><circle cx="40" cy="38" r="1.5" fill="#fff"/></svg>
    <h3>Website Hosting &amp;<br>Management</h3>
    <p>At vero eos et accusamus et iusto odio dignissimos ducimus qu.</p>
  </article>
  <article class="abs service-card" style="left:773px;top:118px">
    <svg width="54" height="46" viewBox="0 0 54 46" fill="none" stroke="#fff" stroke-width="2.4"><rect x="4" y="12" width="36" height="24" rx="2"/><path d="M2 40h44"/><circle cx="40" cy="12" r="10" fill="#fff"/><path d="M35 12l4 4 6-7" stroke="#473d6a" stroke-width="2.6"/></svg>
    <h3>Website Health<br>Check (SEO)</h3>
    <p>At vero eos et accusamus et iusto odio dignissimos ducimus qu.</p>
  </article>
  <article class="abs service-card" style="left:132px;top:360px">
    <svg width="54" height="46" viewBox="0 0 54 46" fill="none" stroke="#fff" stroke-width="2.4"><circle cx="24" cy="20" r="8"/><path d="M24 4v6M24 30v6M8 20h6M34 20h6M13 9l4 4M31 27l4 4M35 9l-4 4M13 31l4-4"/><path d="M30 26l14 16" stroke-width="4"/></svg>
    <h3>Website Updating &amp;<br>Development</h3>
    <p>At vero eos et accusamus et iusto odio dignissimos ducimus qu.</p>
  </article>
  <article class="abs service-card" style="left:453px;top:360px">
    <svg width="54" height="46" viewBox="0 0 54 46" fill="none" stroke="#fff" stroke-width="2.4"><rect x="10" y="2" width="30" height="40" rx="1"/><path d="M40 10h6v30a4 4 0 0 1-4 4H12"/><rect x="15" y="8" width="20" height="8" fill="#fff"/><path d="M15 22h20M15 28h20M15 34h14"/></svg>
    <h3>Newsletter<br>Management</h3>
    <p>At vero eos et accusamus et iusto odio dignissimos ducimus qu.</p>
  </article>
  <article class="abs service-card" style="left:773px;top:360px">
    <svg width="54" height="46" viewBox="0 0 54 46" fill="none" stroke="#fff" stroke-width="2.4"><path d="M6 18L27 4l21 14v24H6z"/><path d="M6 18l21 14 21-14"/><rect x="14" y="10" width="26" height="14" fill="#473d6a"/><path d="M18 14h18M18 19h18"/></svg>
    <h3>Email<br>Management</h3>
    <p>At vero eos et accusamus et iusto odio dignissimos ducimus qu.</p>
  </article>
</section>

<section class="welcome">
  <h2 class="abs">Welcome to our site</h2>
  <div class="abs h-rule"></div>
  <div class="abs welcome-text">
    <p>On the other hand, we denounce with righteous indignation and dislike men who are so beguiled and demoralized by the charms of pleasure of the moment, so blinded by desire, that they cannot foresee the pain and trouble that are bound to ensue; and equal blame belongs to those who fail</p>
    <p>So blinded by desire, that they cannot foresee the pain and trouble that are bound to ensue; and equal blame belongs to those who fail</p>
  </div>
  <a class="btn">Read more <svg width="10" height="10" viewBox="0 0 12 12"><path d="M1 1l5 5-5 5M6 1l5 5-5 5" stroke="#fff" stroke-width="1.6" fill="none"/></svg></a>
  <div class="abs video">
    <div class="video-frame" role="img" aria-label="Video still of two business colleagues talking at a laptop"></div>
    <div class="abs play"><svg width="28" height="30" viewBox="0 0 28 30"><path d="M4 2l22 13L4 28z" fill="#333"/></svg></div>
    <div class="abs progress"><span></span></div>
    <div class="abs controls">
      <svg width="10" height="12" viewBox="0 0 10 12"><path d="M1 1l8 5-8 5z" fill="#ddd"/></svg>
      <span>0:00 / 0:46</span>
      <span style="margin-left:auto;font-size:8px;color:#999">SPEED <b style="color:#ddd;font-size:10px">1.0x</b></span>
      <svg width="14" height="12" viewBox="0 0 14 12"><path d="M1 4h3l4-3v10L4 8H1z" fill="#ddd"/><path d="M10 3c2 2 2 4 0 6" stroke="#ddd" fill="none"/></svg>
      <svg width="14" height="12" viewBox="0 0 14 12"><rect x="1" y="1" width="12" height="10" fill="none" stroke="#ddd"/><rect x="6" y="5" width="6" height="5" fill="#ddd"/></svg>
    </div>
  </div>
</section>

<section class="modules">
  <article class="abs module" style="left:132px">
    <h2>Latest blog</h2>
    <div class="blog-item" style="top:56px"><div class="thumb" role="img" aria-label="Business team meeting photo" style="background:linear-gradient(135deg,#9fb0c6,#3e4e66)"></div><div class="blog-body"><div class="date">02/08/2016</div><h4>At vero eos et accusam</h4><p>On the other hand, we denou nce with righteous.</p></div></div>
    <div class="blog-item" style="top:158px"><div class="thumb" role="img" aria-label="Handshake photo" style="background:linear-gradient(135deg,#c6d3de,#5b7188)"></div><div class="blog-body"><div class="date">02/08/2016</div><h4>But I must explain to you</h4><p>On the other hand, we denou nce with righteous.</p></div></div>
    <div class="blog-item" style="top:260px"><div class="thumb" role="img" aria-label="Financial charts on a desk photo" style="background:linear-gradient(135deg,#d9e6ef,#7d9bb5)"></div><div class="blog-body"><div class="date">02/08/2016</div><h4>On the other hand, we</h4><p>On the other hand, we denou nce with righteous.</p></div></div>
    <a class="btn">Read more blogs</a>
  </article>

  <article class="abs module" style="left:450px">
    <h2>Testimonials</h2>
    <div class="quote-item" style="top:56px"><div class="headshot" role="img" aria-label="Headshot of Daniel Orwell" style="background:linear-gradient(160deg,#c9ced6,#6e7b8c)"></div><div class="quote-body"><span class="quote-mark">“</span><p>At vero eos et accusamus et iusto odio dignissimos du cimus qui ...</p><span class="who">Daniel Orwell</span></div></div>
    <div class="quote-item" style="top:158px"><div class="headshot" role="img" aria-label="Headshot of Simon Hale" style="background:linear-gradient(160deg,#e2e2e2,#8d8d8d)"></div><div class="quote-body"><span class="quote-mark">“</span><p>On the other hand, we denounce with righteous indignation..</p><span class="who">Simon Hale</span></div></div>
    <div class="quote-item" style="top:260px"><div class="headshot" role="img" aria-label="Headshot of Owen" style="background:linear-gradient(160deg,#d6d6d6,#7f7f7f)"></div><div class="quote-body"><span class="quote-mark">“</span><p>debitis aut rerum ne ces sitatibus saepe eveniet ut et voluptates.</p><span class="who">Owen</span></div></div>
    <a class="btn">Read more testimonials</a>
  </article>

  <article class="abs module" style="left:767px">
    <h2>Chatterlane</h2>
    <div class="abs feed-tag"></div>
    <div class="feed-item" style="top:56px"><div class="feed-thumb" style="background:#2a2a2a"></div><div><h4>Contrary to popular belief, Lorem Ipsum is not simply random text.</h4><p>17 people recommended this</p></div></div>
    <div class="feed-item" style="top:136px"><div class="feed-thumb" style="background:#d9c49a"></div><div><h4>It is a long established fact that a reader will be distracted by the</h4><p>2 people recommended this</p></div></div>
    <div class="feed-item" style="top:216px"><div class="feed-thumb" style="background:#8aa0c4"></div><div><h4>There are many variations of passages of Lorem Ipsum.</h4><p>5 people recommended this</p></div></div>
    <div class="feed-item" style="top:296px;border-bottom:none"><div class="feed-thumb" style="background:#eadfc4"></div><div><h4>The standard chunk of Lorem Ipsum used since</h4><p>172 people recommended this</p></div></div>
    <div class="abs plugin-bar"><span></span>Chatterlane social plugin</div>
  </article>
</section>

<footer class="site-footer">
  <div class="abs footer-menu">
    <h4>Menu</h4>
    <ul>
      <li>Digital Marketing About</li>
      <li>Quorvo Promoline Contact</li>
      <li>Chatterlane Advertising Privacy Policy</li>
      <li>Search Engine Optimisation (SEO) Terms &amp; Conditions</li>
      <li>Website Hosting FAQ</li>
      <li>Newsletter Management</li>
    </ul>
  </div>
  <div class="abs company">
    <h4>Company information</h4>
    <address>Brightcrest<br>14 Marlow Close<br>Bracknell<br>Berskhire<br>ZZ9 4QT<br>Tel: 01632 960481</address>
  </div>
  <div class="abs social" aria-label="Chatterlane, Pipwave and Careernest">
    <span style="background:#3b5998"></span><span style="background:#1da1f2"></span><span style="background:#0e76a8"></span>
  </div>
  <div class="abs map" role="img" aria-label="Quorvo location map of Bracknell"></div>
  <div class="abs footer-rule"></div>
  <div class="abs copyright">Copyrihgts @ 2016 All Rights Reserved</div>
</footer>

</body>
</html>
```